Heritage Hollow Business Cards

Require a business card design. <br/><br/>Needs to include logo (either round or long version) plus these details:<br/>Maya Torvel<br/>Heritage Hollow<br/>maya@quonbrook.com.au<br/>02 6481 7390<br/>PO Box Glenwarra NSW 2913<br/>www.heritagehollow.com.au<br/><br/>I need in an editable format so that I can create for multiple staff members. <br/><br/>

Target Market(s)

We are an online store selling renovation products to home owners are builders. Looking for a classic classy design.

Industry/Entity Type

Home And Garden

Contact Information for Business Card

Maya Torvel
Heritage Hollow
maya@quonbrook.com.au
02 6481 7390
PO Box Glenwarra NSW 2913
www.heritagehollow.com.au

Colors

Designer to choose colors to be used in the design.

Requirements
Must have
• Must include Logo.

```html
<!DOCTYPE html>
<html lang="en">
<head>
<meta charset="utf-8">
<title>Heritage Hollow Business Cards</title>
<link href="https://fonts.googleapis.com/css2?family=Work+Sans:wght@400;500;700&display=swap" rel="stylesheet">
<style>
  :root {
    --backdrop: #e4e4e6;
    --card: #1d1d1d;
    --card-edge: #262626;
    --ink: #ffffff;
    --ink-muted: #8a8a8a;
    --rule: #6f6f6f;
  }
  * { box-sizing: border-box; margin: 0; padding: 0; }
  html, body {
    width: 1200px; height: 900px; overflow: hidden;
    background: var(--backdrop);
    font-family: "Work Sans", Arial, sans-serif;
  }
  .stage {
    width: 1200px; height: 900px;
    display: flex; flex-direction: column; align-items: center; justify-content: center;
    gap: 40px;
  }
  .card {
    position: relative;
    width: 700px; height: 390px;
    background: linear-gradient(135deg, var(--card-edge), var(--card) 60%);
    box-shadow: 0 6px 16px rgba(0,0,0,0.25);
    color: var(--ink);
  }
  /* Front */
  .brand-mark {
    position: absolute; left: 50%; top: 38px; transform: translateX(-50%);
    width: 250px; height: 250px;
    border: 1px solid rgba(255,255,255,0.75); border-radius: 50%;
    display: flex; align-items: center; justify-content: center; text-align: center;
  }
  .brand-name {
    font-weight: 500; font-size: 34px; line-height: 1.1; color: var(--ink);
  }
  .front-url {
    position: absolute; left: 0; right: 0; bottom: 52px; text-align: center;
    font-size: 15px; letter-spacing: 4px; font-weight: 500;
  }
  /* Back */
  .identity {
    position: absolute; left: 50px; top: 150px; width: 215px; text-align: right;
  }
  .person-name { font-weight: 700; font-size: 32px; letter-spacing: 1px; }
  .person-role { font-size: 18px; margin-top: 4px; }
  .person-company { font-size: 18px; color: var(--ink-muted); margin-top: 2px; }
  .divider {
    position: absolute; left: 290px; top: 148px; width: 1px; height: 128px; background: var(--rule);
  }
  .contact {
    position: absolute; left: 318px; top: 148px; font-size: 18px; line-height: 1.3;
  }
  .address { padding-left: 12px; margin-bottom: 6px; }
  .contact-row { display: flex; align-items: center; gap: 10px; }
  .contact-row svg { width: 16px; height: 16px; flex: none; }
  .url-domain { color: var(--ink-muted); }
</style>
</head>
<body>
<main class="stage">
  <section class="card card-front">
    <div class="brand-mark">
      <span class="brand-name">Heritage<br>Hollow</span>
    </div>
    <p class="front-url">www.heritagehollow.com.au</p>
  </section>

  <section class="card card-back">
    <div class="identity">
      <p class="person-name">Maya Torvel</p>
      <p class="person-role">Director</p>
      <p class="person-company">Heritage Hollow</p>
    </div>
    <div class="divider"></div>
    <div class="contact">
      <p class="address">PO Box Glenwarra<br>NSW 2913</p>
      <p class="contact-row">
        <svg viewBox="0 0 16 16" fill="none" stroke="#9a9a9a" stroke-width="1.4"><path d="M4 2l2 3-1.5 1.5c.8 1.8 2.2 3.2 4 4L10 9l3 2-1.5 2.5C7 13 3 9 2.5 4.5z"/></svg>
        02 6481 7390
      </p>
      <p class="contact-row">
        <svg viewBox="0 0 16 16" fill="none" stroke="#9a9a9a" stroke-width="1.4"><rect x="1.5" y="3.5" width="13" height="9"/><path d="M1.5 3.5l6.5 5 6.5-5"/></svg>
        maya@quonbrook.com.au
      </p>
      <p class="contact-row">
        <svg viewBox="0 0 16 16" fill="none" stroke="#9a9a9a" stroke-width="1.2"><circle cx="8" cy="8" r="6.5"/><ellipse cx="8" cy="8" rx="3" ry="6.5"/><path d="M1.5 8h13M2.5 5h11M2.5 11h11"/></svg>
        <span>www.<span class="url-domain">heritagehollow</span>.com.au</span>
      </p>
    </div>
  </section>
</main>
</body>
</html>
```